Bramble Systems Voip Broucher

We require a full page broucher 8.5X11 format for a Voip promotion
Updates

Target Market(s)

Business Customer

Industry/Entity Type

Voip

Colors
ec1f27
0592cd

Requirements
Must have
• Logo, Information as provided, our phone number 1-877-555-0193, Colors that match the logo. Reds, blues and white please.

```html
<!DOCTYPE html>
<html lang="en">
<head>
<meta charset="utf-8">
<title>Bramble Systems VoIP Brochure</title>
<link href="https://fonts.googleapis.com/css2?family=Titillium+Web:wght@300;400;600;700&family=Open+Sans:wght@400;600&display=swap" rel="stylesheet">
<style>
:root{
  --red:#d71f27;
  --red-dark:#a8161d;
  --red-text:#c4161c;
  --ink:#333;
  --charcoal:#3a3a3c;
  --grey-box:#8a8a8c;
  --grey-panel:#ececec;
  --page:#ffffff;
  --bg:#e4e4e4;
  --photo-a:#d9c7b6;
  --photo-b:#7f8b99;
  --photo-blue-a:#1b4f8a;
  --photo-blue-b:#c9d9ea;
  --handset:#1f1f22;
}
*{box-sizing:border-box;margin:0;padding:0}
html,body{width:1200px;height:837px;overflow:hidden;background:var(--bg)}
body{position:relative;font-family:"Open Sans",Arial,sans-serif;color:var(--ink)}
.page{position:absolute;top:56px;width:560px;height:724px;background:var(--page);overflow:hidden;box-shadow:0 2px 8px rgba(0,0,0,.15)}
.page--front{left:25px}
.page--back{left:615px}
.abs{position:absolute}
.photo{position:absolute}
.shapes{position:absolute;left:0;top:0;z-index:1}
.headline,.brand,.handset,.call,.bar-text{z-index:2}
.headline{position:absolute;font-family:"Titillium Web",Arial,sans-serif;color:#fff;font-weight:300;font-size:21px;line-height:27px;text-transform:uppercase}
.headline strong{font-weight:700}
.brand{position:absolute;font-family:"Titillium Web",Arial,sans-serif;font-weight:600;color:var(--red-dark);font-size:26px;display:flex;align-items:center;gap:8px;letter-spacing:.5px}
.brand-mark{width:14px;height:14px;background:var(--red-dark)}
.handset{position:absolute;border-radius:10px;background:linear-gradient(150deg,#3a3a3e,var(--handset))}
.section-title{font-family:"Titillium Web",Arial,sans-serif;font-weight:600;color:var(--red-text);font-size:13px;margin-bottom:6px}
.features{list-style:none;font-size:10px;line-height:11.5px}
.features li{position:relative;padding-left:17px;margin-bottom:8px}
.features li::before{content:"";position:absolute;left:0;top:1px;width:10px;height:10px;background:var(--red)}
.features li::after{content:"";position:absolute;left:3px;top:2px;width:3px;height:6px;border:solid #fff;border-width:0 1.6px 1.6px 0;transform:rotate(45deg)}
.detail{font-size:9px;line-height:11px;margin-top:4px}
.detail b{display:block;color:var(--red-text);font-weight:600}
.cost-box{position:absolute;left:319px;top:374px;width:241px;height:270px;background:var(--grey-box);color:#fff;padding:16px 14px;font-size:12.5px;line-height:15px}
.cost-box h2{font-family:"Titillium Web",Arial,sans-serif;font-weight:700;font-size:18px;margin-bottom:8px}
.cost-box p{margin-bottom:14px;text-align:justify}
.call{position:absolute;color:#fff;font-family:"Titillium Web",Arial,sans-serif}
.call-label{font-size:15px;font-weight:600;line-height:18px}
.call-number{font-size:25px;font-weight:600;line-height:30px}
.bar-text{position:absolute;color:#fff;font-family:"Titillium Web",Arial,sans-serif;font-weight:600;font-size:13.5px}
.qa{position:absolute;left:20px;top:359px;width:520px;height:274px;background:var(--grey-panel);padding:9px 14px}
.qa h2{font-family:"Titillium Web",Arial,sans-serif;font-weight:600;color:var(--red-text);font-size:16px;margin-bottom:5px}
.qa-cols{display:flex;gap:22px}
.qa-col{flex:1;font-size:9px;line-height:12px;color:#444}
.qa-item{margin-bottom:10px;text-align:justify}
</style>
</head>
<body>

<section class="page page--front">
  <div class="photo" role="img" aria-label="Smiling call centre agent wearing a headset, colleagues blurred behind" style="left:0;top:0;width:560px;height:300px;background:linear-gradient(110deg,var(--photo-a),#efe6dc 45%,var(--photo-b))"></div>
  <svg class="shapes" width="560" height="724" viewBox="0 0 560 724" aria-hidden="true">
    <polygon points="0,228 560,288 560,347 0,393" fill="var(--red)"/>
    <polygon points="0,228 330,264 250,393 0,393" fill="var(--red-dark)" opacity=".35"/>
    <polygon points="0,633 160,633 205,724 0,724" fill="var(--red)"/>
    <polygon points="0,633 25,618 25,633" fill="var(--red)"/>
    <polygon points="185,670 560,670 560,710 206,710" fill="var(--charcoal)"/>
  </svg>
  <div class="handset" role="img" aria-label="Desk VoIP phone with colour video display and coiled cord" style="left:330px;top:178px;width:170px;height:190px;transform:rotate(-8deg)"></div>
  <h1 class="headline" style="left:20px;top:292px">Upgrade your office<br>phone system and<br><strong>Cut your phone bill in half</strong></h1>

  <div class="brand" style="left:30px;top:402px"><span class="brand-mark"></span>Bramble Systems</div>

  <div class="abs" style="left:29px;top:462px;width:270px">
    <h2 class="section-title">What do you get?</h2>
    <ul class="features">
      <li>Modern Office phone system with the latest features only available through Voice over IP</li>
      <li>Installation and ongoing support services as required</li>
      <li>Unlimited local and long distance calling within North America only</li>
    </ul>
    <p class="detail"><b>Included phone feature set:</b>Auto attendant, Voicemail, 3 ways calling, hands free, call forward, Intercom, email tie in.</p>
    <p class="detail"><b>Support Services:</b>hardware installation, training, ongoing support,</p>
  </div>

  <div class="cost-box">
    <h2>What does it cost?</h2>
    <p>Flat monthly fee of $25.00 per month per desk phone</p>
    <p>Costing for a hypothetical Example:</p>
    <p>Nation Administration office has 35 office phones. What will it cost to upgrade the office and what will the monthly cost be?</p>
    <p>$25.00 line fee x 35 handsets = $875.00 per month.</p>
  </div>

  <div class="call" style="left:19px;top:654px">
    <div class="call-label">CALL US NOW</div>
    <div class="call-number">877 555 0193</div>
  </div>
  <div class="bar-text" style="left:216px;top:681px">Cedar Court - 4410 Harlow Ave Brookfield, Alberta T9X 2K</div>
</section>

<section class="page page--back">
  <div class="photo" role="img" aria-label="Support agent with headset beside a row of office computer monitors and a globe of binary code" style="left:0;top:0;width:560px;height:190px;background:linear-gradient(100deg,#e9eef4,var(--photo-blue-a) 45%,var(--photo-blue-b))"></div>
  <div class="qa">
    <h2>Q &amp; A</h2>
    <div class="qa-cols">
      <div class="qa-col">
        <p class="qa-item">Q How does it work?<br>A Rather than calls coming and going through Northline phone lines, calls get routed to the exchange through the internet connection.</p>
        <p class="qa-item">Q Is this a new and is it reliable<br>A This technology has been around for over a decade. Its works very well and is used across the globe.</p>
        <p class="qa-item">Q Can I keep our offices existing telephone number?<br>A Yes, we can port the existing number</p>
        <p class="qa-item">Q Is there 911 services<br>A Yes, we register your legal land description with E911 and 911 calling is available</p>
      </div>
      <div class="qa-col">
        <p class="qa-item">Q Can we fax using VoIP<br>A Yes faxing works fine through VoIP.</p>
        <p class="qa-item">Q What does it cost to upgrade the handset to a colour display phone that supports video calling?<br>A one-time fee of $100 per handset to move to colour. Colour handsets also supports video calling</p>
        <p class="qa-item">Q What costs are not included to get the new phone system in place.<br>A The new phone system run through ethernet office network cabling. Your office may need the cabling upgraded to allow use of VoIP phones. We can provide an affordable estimate to improve your cabling to support a VoIP phone.<br>A The calls will route through your existing office internet connection.</p>
      </div>
    </div>
  </div>
  <svg class="shapes" width="560" height="724" viewBox="0 0 560 724" aria-hidden="true">
    <polygon points="0,149 560,110 560,272 0,230" fill="var(--red)"/>
    <polygon points="0,633 160,633 205,724 0,724" fill="var(--red)"/>
    <polygon points="0,633 23,620 23,633" fill="var(--red)"/>
    <polygon points="185,669 560,669 560,710 206,710" fill="var(--charcoal)"/>
  </svg>
  <div class="handset" role="img" aria-label="Desk VoIP phone with colour app display and coiled cord" style="left:40px;top:148px;width:180px;height:168px"></div>
  <h1 class="headline" style="right:18px;top:152px;text-align:right">Upgrade your office<br>phone system and<br><strong>Cut your phone bill in half</strong></h1>

  <div class="brand" style="right:25px;top:300px"><span class="brand-mark"></span>Bramble Systems</div>

  <div class="call" style="left:19px;top:654px">
    <div class="call-label">CALL US NOW</div>
    <div class="call-number">877 555 0193</div>
  </div>
  <div class="bar-text" style="right:32px;top:678px;font-size:18px">www.bramblesys.net</div>
</section>

</body>
</html>
```